Nutrition-Cooking Website

Hello!
I am in a need of a lovely looking website for my new nutrition practice. I am looking for something sleek, sophisticated, professional yet also welcoming.

Here is a current layout which can be tweaked or overhauled. I feel like the website is not quite what I want so thats why I need your help!!
http://tolvanfolio.example/RENATA-OSSLER-concept-15/

Two websites I like are: (layout similar to www.marquetta.example) or http://www.pernillavostraken.example

Here are the tabs for the website:
About Registered Dietitian Healthy Recipes Philanthropy Shop Features Contact Blog

Features for the Home page include:
Slideshow with 3 rotating updates (like www.marquetta.example)
Video Box (like www.marquetta.example)
Recent Recipes (like http://harrowfield7731.example)
Recent Posts (like http://harrowfield7731.example)
Food Knowledge Box- quick tidbits on laws on food (like www.marquetta.example- she has food wisdom)
Tried and True Benefits of Mediterranean Cuisine (like www.marquetta.example)
Picture of me with brief quote/bio (like www.bettinoruval.example)
Social media buttons

Color Scheme:
• I like the white with gold embroidery or the pretty bluish/purplish in the first pic would be awesome with the slight pink undertones (http://glossedtwirl.example/2012/10/quorvel-marigelle-collection-by-tansley/)
• Also like this goldish background- exotic/sophisticated- http://www.thewhirlingcook.example/Home.html
• Also like the rustic goldish look in the background like this-
ohttp://img.prentlo.example/vexomarks_rsvp_vintage_rustic_gold_swirls_invitation-p161658028764768924bebn6_400.jpg
o http://img.prentlo.example/vexomarks_ornamental_rustic_gold_swirls_invitation-p161776340110432961bvddb_400.jpg
• maybe can have the vines as grapes/olives
OPEN TO ALL DIFFERENT COLORS SCHEMES- whatever looks, clean, sophisticated and professional

Logo:
• Attached is the logo

Budget is flexible. If you think you can improve the website- please do so :)

Target Market(s)

health conscious individuals of all ages

Industry/Entity Type

Embroidery

Requirements
Must have
• clean and sharp look
professional looking
Should not have
• too much busyness

```html
<!DOCTYPE html>
<html lang="en">
<head>
<meta charset="utf-8">
<title>Renata Ossler RD – Home</title>
<link href="https://fonts.googleapis.com/css2?family=Play&family=Open+Sans:wght@400;600&display=swap" rel="stylesheet">
<style>
:root{
  --bg:#efe9dc;
  --page:#ffffff;
  --gold:#e4d6bd;
  --gold-dark:#b59a57;
  --tab:#ecdcc4;
  --ink:#1e1e1e;
  --text:#555555;
  --muted:#8a8a8a;
  --line:#dddddd;
  --accent:#c0143c;
  --link:#b48a3c;
  --sky:#2a9fd6;
  --foot:#262626;
  --foot-deep:#1d1d1d;
  --foot-text:#9a9a9a;
}
*{box-sizing:border-box;margin:0;padding:0}
html,body{width:818px;height:1200px;overflow:hidden}
body{background:var(--bg);font-family:"Open Sans",sans-serif;color:var(--text);position:relative}
.page{position:absolute;left:82px;top:0;width:655px;height:1200px;background:var(--page)}
.abs{position:absolute}
.topline{left:0;top:7px;width:655px;height:4px;background:var(--gold)}
.drop-tab{left:624px;top:11px;width:23px;height:12px;background:var(--gold);border-radius:0 0 3px 3px}
.drop-tab svg{display:block;margin:3px auto 0}
.brand{left:10px;top:30px;font-family:"Play",sans-serif;font-size:23px;letter-spacing:2.5px;color:var(--ink)}
.follow-top{left:532px;top:34px;font-size:9px;color:#444}
.social{display:flex;gap:11px}
.social span{width:11px;height:11px;border-radius:50%;background:#e0cfae;display:block}
.follow-top .social{margin-top:8px}
.nav{left:7px;top:76px;width:640px;height:36px;border-bottom:3px solid var(--gold);display:flex;font-size:10.5px;color:var(--ink)}
.nav a{color:inherit;text-decoration:none;padding:12px 0 0;position:absolute;top:0;height:33px}
.nav .current{background:var(--tab);width:48px;text-align:center;left:0}
.panel{border:1px solid var(--line);background:#fff}
.slider{left:7px;top:122px;width:641px;height:297px}
.thumb{width:207px;height:90px;left:5px}
.cap{position:absolute;left:0;bottom:0;width:100%;height:24px;background:rgba(40,40,40,.72);color:#fff;font-family:"Play",sans-serif;font-size:16px;text-align:center;line-height:24px}
.hero{left:222px;top:5px;width:413px;height:283px;background:radial-gradient(ellipse at 45% 50%,#c9a36a 0%,#a8572a 40%,#7a3518 75%,#efe0d0 100%)}
.hero-cap{position:absolute;left:0;bottom:0;width:100%;height:42px;background:rgba(235,228,220,.78);font-family:"Play",sans-serif;font-size:16px;color:#555;padding:13px 0 0 19px}
.dots{position:absolute;right:42px;top:18px;display:flex;gap:4px}
.dots span{width:9px;height:9px;border-radius:50%;background:#fff;border:2px solid #ccc}
.dots .on{background:#d9c27a;border-color:#d9c27a}
.arrow{position:absolute;top:120px;width:22px;height:26px;background:rgba(235,235,235,.8);border-radius:50%;display:flex;align-items:center;justify-content:center}
.h2{font-family:"Play",sans-serif;font-size:16px;color:var(--ink)}
.bio{left:7px;top:434px;width:387px;height:151px}
.bio-photo{left:6px;top:7px;width:107px;height:134px;border:1px solid var(--line);padding:5px}
.bio-photo div{width:100%;height:100%;background:linear-gradient(180deg,#f2f0ee,#e7c9c0 60%,#d3537f)}
.bio .h2{left:121px;top:9px}
.bio-text{left:121px;top:33px;width:230px;font-size:8.4px;line-height:10.5px;text-align:justify;color:#444}
.bio-text p+p{margin-top:10.5px}
.posts{left:7px;top:597px;width:387px;height:203px}
.posts .h2{left:7px;top:8px}
.post{left:7px;width:370px;height:70px}
.post-img{width:87px;height:58px}
.post-title{left:93px;top:-3px;color:var(--accent);font-size:10.4px}
.post-text{left:93px;top:14px;width:275px;font-size:8.4px;line-height:15px;color:#555}
.more{right:0;top:56px;font-size:8.4px;color:var(--link)}
.viewall{font-size:8.4px;color:var(--link);letter-spacing:.5px}
.recipes{left:403px;top:434px;width:245px;height:366px}
.recipes .h2{left:7px;top:16px;font-size:17px}
.tabs{left:166px;top:7px;display:flex;font-size:8.5px;color:#444;text-align:center}
.tabs div{width:38px;height:28px;padding-top:3px}
.tabs .sel{background:var(--tab)}
.tabs i{display:block;width:7px;height:7px;border-radius:50%;border:1.5px solid #555;margin:0 auto 2px}
.recipe{left:5px;width:233px;height:72px;border-bottom:1px solid #e5e5e5}
.recipe-img{width:79px;height:58px}
.recipe-title{left:86px;top:-2px;font-size:9px;color:var(--accent);letter-spacing:.5px}
.stars{left:86px;top:9px;font-size:10px;color:var(--accent);letter-spacing:-1px}
.stars b{color:#ccc;font-weight:400}
.recipe-links{left:86px;top:24px;font-size:7.6px;line-height:12.3px;color:#555;letter-spacing:.4px}
.video{left:7px;top:813px;width:641px;height:173px}
.video-img{left:6px;top:12px;width:275px;height:146px;background:linear-gradient(120deg,#1e3ca8,#3f5fd0 40%,#7b78c8 60%,#2a2f8f)}
.play{left:115px;top:55px;width:46px;height:28px;background:rgba(40,40,40,.75);border-radius:3px;display:flex;align-items:center;justify-content:center}
.video .h2{left:295px;top:10px;font-size:13.5px}
.video-text{left:295px;top:30px;width:340px;font-size:8.4px;line-height:15px;color:#555}
.tweet{left:0;top:1000px;width:655px;height:30px;background:var(--sky);color:#fff;font-size:8.4px;display:flex;align-items:center;justify-content:center;gap:7px}
.tweet span.dot{width:11px;height:11px;border-radius:50%;background:#dff1fb}
.footer{left:0;top:1030px;width:655px;height:140px;background:var(--foot)}
.fcol{top:15px;color:#eee}
.fcol h3{font-family:"Play",sans-serif;font-weight:400;font-size:12px;margin-bottom:9px}
.fcol ul{list-style:none;font-size:7.4px;line-height:16.4px;color:var(--foot-text)}
.fcol li::before{content:"";display:inline-block;width:3px;height:3px;border-radius:50%;background:#888;margin:0 7px 1px 0;vertical-align:middle}
.news h3{font-family:"Play",sans-serif;font-weight:400;font-size:12px;color:#eee}
.news-form{margin-top:6px;width:177px;height:22px;background:#fff;border-radius:3px;display:flex;align-items:center;padding:0 3px 0 11px;font-size:7.4px;color:#888}
.news-form b{margin-left:auto;background:#e8dcc6;width:34px;height:17px;font-weight:600;font-size:8.5px;color:#333;display:flex;align-items:center;justify-content:center}
.news .social{margin-top:9px}
.news .social span{background:#cfcfcf}
.copy{left:0;top:1170px;width:655px;height:30px;background:var(--foot-deep);font-size:8px;color:#888;padding:9px 0 0 16px}
</style>
</head>
<body>
<div class="page">
  <div class="abs topline"></div>
  <div class="abs drop-tab"><svg width="9" height="5" viewBox="0 0 9 5"><path d="M0 0h9L4.5 5z" fill="#b59a57"/></svg></div>
  <div class="abs brand">RENATA OSSLER RD</div>
  <div class="abs follow-top">Follow Us :<div class="social"><span></span><span></span><span></span><span></span></div></div>

  <nav class="abs nav">
    <a class="current" href="#">Home</a>
    <a href="#" style="left:61px">About</a>
    <a href="#" style="left:113px">Registered Dietitian</a>
    <a href="#" style="left:230px">Healthy Recipes</a>
    <a href="#" style="left:328px">Philanthropy</a>
    <a href="#" style="left:411px">Shop</a>
    <a href="#" style="left:458px">Features</a>
    <a href="#" style="left:522px">Contact</a>
    <a href="#" style="left:583px">Blog</a>
  </nav>

  <section class="abs panel slider">
    <div class="abs thumb" style="top:5px;background:linear-gradient(160deg,#f3e7c4,#d94a2a 45%,#e9cf8c)" role="img" aria-label="Plate of pasta with tomato sauce and herbs"><div class="cap">Food Knowledge</div></div>
    <div class="abs thumb" style="top:101px;background:linear-gradient(160deg,#b98a52,#8e9a4a 45%,#c59b62)" role="img" aria-label="Bowl of grain salad with herbs"><div class="cap">Food Philosophy</div></div>
    <div class="abs thumb" style="top:199px;background:linear-gradient(160deg,#f0ece4,#f08a5a 40%,#e96d3a 70%,#f4e5d3)" role="img" aria-label="Plate of cooked shrimp with parsley"><div class="cap">Mediterranean Cuisine</div></div>
    <div class="abs hero" role="img" aria-label="Bowl of shredded papaya salad with peanuts">
      <div class="arrow" style="left:2px"><svg width="8" height="12" viewBox="0 0 8 12"><path d="M7 1 2 6l5 5" stroke="#333" stroke-width="2" fill="none"/></svg></div>
      <div class="arrow" style="right:2px"><svg width="8" height="12" viewBox="0 0 8 12"><path d="m1 1 5 5-5 5" stroke="#333" stroke-width="2" fill="none"/></svg></div>
      <div class="hero-cap">Welcome to Renata Ossler RD<div class="dots"><span class="on"></span><span></span><span></span></div></div>
    </div>
  </section>

  <section class="abs panel bio">
    <div class="abs bio-photo"><div role="img" aria-label="Portrait of a smiling woman holding a bowl"></div></div>
    <h2 class="abs h2">Priya Valdane</h2>
    <div class="abs bio-text">
      <p>“Although I grew up in the west, coming home every day was like entering a little Indian colony. I was always welcomed in by the spicy smells emanating from the kitchen. Cooking Indian food keeps me close to my roots; and is the most important way I remain healthy.</p>
      <p>People’s experience of eating Indian food in the west is not a true reflection of the real food we eat at home, which is lighter, fresher and far more well balanced than the offerings at Indian restaurants.</p>
    </div>
  </section>

  <section class="abs panel posts">
    <h2 class="abs h2">Recent Post</h2>
    <article class="abs post" style="top:33px">
      <div class="abs post-img" style="background:linear-gradient(135deg,#6a9a2a,#d8344a 50%,#f0a030)" role="img" aria-label="Fresh fruit salad"></div>
      <div class="abs post-title">Fresh Summer Fruit Salad</div>
      <div class="abs post-text">Lorem Ipsum is simply dummy text of the printing and typesetting industry. Lorem Ipsum has been the industry's standard dummy text ever since the 1500s,</div>
      <div class="abs more">Read More ⟶</div>
    </article>
    <article class="abs post" style="top:111px">
      <div class="abs post-img" style="background:linear-gradient(135deg,#3a1a1a,#b8202a 50%,#e9d0c8)" role="img" aria-label="Berry desserts in glasses"></div>
      <div class="abs post-title">Delicious Berry Desserts</div>
      <div class="abs post-text">Lorem Ipsum is simply dummy text of the printing and typesetting industry. Lorem Ipsum has been the industry's standard dummy text ever since the 1500s,</div>
      <div class="abs more">Read More ⟶</div>
    </article>
    <div class="abs viewall" style="right:8px;top:183px">View All »</div>
  </section>

  <section class="abs panel recipes">
    <h2 class="abs h2">Recent Recipes</h2>
    <div class="abs tabs"><div><i></i>Popular</div><div class="sel"><i></i>Latest</div></div>
    <article class="abs recipe" style="top:45px">
      <div class="abs recipe-img" style="background:linear-gradient(135deg,#4a5a2a,#c9a040 50%,#6f8a30)" role="img" aria-label="Spicy ginger chicken in a pan"></div>
      <div class="abs recipe-title">Spicy Ginger Chicken</div>
      <div class="abs stars">★★★★<b>★</b></div>
      <div class="abs recipe-links">View Recipe<br>Email Recipe<br>Save to My Recipe Box</div>
    </article>
    <article class="abs recipe" style="top:123px">
      <div class="abs recipe-img" style="background:linear-gradient(135deg,#f2e0c8,#d98a3a 50%,#5a8a3a)" role="img" aria-label="Sautéed chicken breast with green beans"></div>
      <div class="abs recipe-title">Chicken Breast Saute Sec</div>
      <div class="abs stars">★★★★<b>★</b></div>
      <div class="abs recipe-links">View Recipe<br>Email Recipe<br>Save to My Recipe Box</div>
    </article>
    <article class="abs recipe" style="top:201px">
      <div class="abs recipe-img" style="background:linear-gradient(135deg,#eef0ea,#a85a30 50%,#5a2a1a)" role="img" aria-label="Crisp pork belly slices"></div>
      <div class="abs recipe-title">Crisp pork belly</div>
      <div class="abs stars">★★★★<b>★</b></div>
      <div class="abs recipe-links">View Recipe<br>Email Recipe<br>Save to My Recipe Box</div>
    </article>
    <article class="abs recipe" style="top:279px;border-bottom:0">
      <div class="abs recipe-img" style="background:linear-gradient(135deg,#2a2a2a,#c8a070 50%,#3a3a3a)" role="img" aria-label="Tray of small pastries"></div>
      <div class="abs recipe-title">Hunter pastry</div>
      <div class="abs stars">★★★★<b>★</b></div>
      <div class="abs recipe-links">View Recipe<br>Email Recipe<br>Save to My Recipe Box</div>
    </article>
    <div class="abs viewall" style="right:8px;top:349px">View All »</div>
  </section>

  <section class="abs panel video">
    <div class="abs video-img" role="img" aria-label="Video still of a woman by a blue dome">
      <div class="abs play"><svg width="14" height="16" viewBox="0 0 14 16"><path d="M0 0l14 8-14 8z" fill="#fff"/></svg></div>
    </div>
    <h2 class="abs h2">Play The Video Renata Ossler RD</h2>
    <div class="abs video-text">
      <p>Lorem Ipsum is simply dummy text of the printing and typesetting industry. Lorem Ipsum has been the industry's standard dummy text ever since the 1500s, when an unknown printer took a galley of type and scrambled it to make a type specimen book.</p>
      <p style="margin-top:15px">It has survived not only five centuries, but also the leap into electronic typesetting, remaining essentially unchanged.<br>It was popularised in the 1960s with the release of Letraset sheets containing Lorem Ipsum passages,</p>
    </div>
  </section>

  <div class="abs tweet"><span class="dot"></span>Lorem Ipsum is simply dummy text of the printing and typesetting industry.http:// RENATA-OSSLER RD</div>

  <footer class="abs footer">
    <div class="abs fcol" style="left:16px"><h3>Home</h3><ul><li>Home</li><li>About Us</li><li>Registered Dietitian</li><li>Healthy Recipes</li><li>Contact Us</li></ul></div>
    <div class="abs fcol" style="left:135px"><h3>More Information</h3><ul><li>Lorem ipsum dolor sit amet</li><li>onsectetuer adipiscing elit</li><li>sed diam nonummy nibh</li><li>Vivamus a felis.</li><li>Proin id massa.</li></ul></div>
    <div class="abs fcol" style="left:305px"><h3>Contact Us</h3><ul><li>est usus legentis in iis qui</li><li>feugiat nulla facilisis at vero</li><li>est usus legentis in iis qui</li><li>fiant sollemnes in futurum.</li><li>luptatum zzril delenit augue</li></ul></div>
    <div class="abs news" style="left:464px;top:26px">
      <h3>NEWS LETTER</h3>
      <div class="news-form">Enter your Email Address<b>Go</b></div>
      <h3 style="margin-top:9px">Follow Us</h3>
      <div class="social"><span></span><span></span><span></span><span></span></div>
    </div>
  </footer>
  <div class="abs copy">Copyright 2013. Renata-Ossler RD . All Rights Reserved.</div>
</div>
</body>
</html>
```